Need Bold, Hip Card for Concert Ticket Website Gleaming Passes!

Hi there! I am putting together a business/website that sells event tickets (mostly concerts, but also some sports and theater). Think SeatNook, but much smaller. The site is called Gleaming Passes. I have a new logo (attached, with black/red/white color scheme), and am looking for a modern/cool/original business card design. Note that I am thinking of having the card itself in the shape of a ticket (die cut), so you may want to keep that in mind when designing, but I'm not set on that. I'm also open to alternative card sizes, thicknesses, glossy, spot UV, etc. in order to stand out. I'm attaching a potential die cut template and a sample card using that template in case you want to work with that.
Target Market(s)
Music fans, people that like going to see live events
Industry/Entity Type
Entertainment
Contact Information for Business Card
Information that I'd like to have:
website address - www.gleamingpasses.example
phone number: 1-833-5GLEAMNG (532-6264)
my name - Wendel Pike

```html
<!DOCTYPE html>
<html lang="en">
<head>
<meta charset="utf-8">
<title>Gleaming Passes – Business Card</title>
<link rel="stylesheet" href="https://fonts.googleapis.com/css2?family=Source+Sans+3:wght@400;600;700&display=swap">
<style>
  :root {
    --ticket-red: #8c0000;
    --ink: #0b0b0b;
    --paper: #ffffff;
    --stage: #ece8e3;
    --muted: #2a2a2a;
  }
  * { margin: 0; padding: 0; box-sizing: border-box; }
  html, body { width: 1064px; height: 1200px; overflow: hidden; }
  body {
    background: var(--stage);
    font-family: "Source Sans 3", "Myriad Pro", Arial, sans-serif;
    position: relative;
  }
  .card {
    position: absolute;
    left: 213px;
    width: 673px;
    height: 416px;
  }
  .card--front { top: 168px; }
  .card--back { top: 631px; }
  .card__shape { position: absolute; inset: 0; width: 673px; height: 416px; }

  .contact-list {
    position: absolute;
    left: 39px;
    top: 182px;
    list-style: none;
    color: var(--paper);
    font-size: 17.5px;
    line-height: 24px;
  }
  .contact-list li { display: flex; align-items: center; gap: 9px; }
  .contact-list svg { width: 13px; height: 13px; flex: none; fill: var(--paper); }
  .address {
    position: absolute;
    left: 39px;
    top: 292px;
    color: var(--paper);
    font-size: 17.5px;
    line-height: 24px;
  }

  .brand {
    position: absolute;
    left: 352px;
    top: 142px;
    display: flex;
    align-items: center;
    gap: 12px;
  }
  .brand__mark { width: 38px; height: 38px; background: var(--ticket-red); flex: none; }
  .brand__name {
    font-weight: 700;
    font-size: 33px;
    line-height: 34px;
    letter-spacing: 1.5px;
    text-transform: uppercase;
    color: var(--ticket-red);
  }

  .person {
    position: absolute;
    right: 43px;
    top: 308px;
    text-align: right;
  }
  .person__name {
    font-size: 23px;
    line-height: 26px;
    font-weight: 600;
    text-transform: uppercase;
    color: var(--ticket-red);
  }
  .person__name .surname { color: var(--ink); }
  .person__role { font-size: 17.5px; line-height: 22px; color: var(--muted); }

  .back-brand {
    position: absolute;
    inset: 0;
    display: flex;
    align-items: center;
    justify-content: center;
    font-weight: 700;
    font-size: 64px;
    line-height: 72px;
    color: var(--paper);
    text-align: center;
  }
</style>
</head>
<body>

<section class="card card--front" aria-label="Business card front">
  <svg class="card__shape" viewBox="0 0 673 416" aria-hidden="true">
    <defs>
      <clipPath id="front-die-cut">
        <path d="M27,0 H646 A27,27 0 0 0 673,27 V389 A27,27 0 0 0 646,416 H27 A27,27 0 0 0 0,389 V27 A27,27 0 0 0 27,0 Z"/>
      </clipPath>
    </defs>
    <g clip-path="url(#front-die-cut)">
      <rect width="673" height="416" fill="var(--paper)"/>
      <path class="red-panel" d="M0,62 Q160,40 317,0 V356 Q160,356 0,367 Z" fill="var(--ticket-red)"/>
      <circle cx="112" cy="62" r="68" fill="var(--paper)"/>
      <path class="base-band" d="M0,384 Q190,368 367,368 V416 H0 Z" fill="var(--ink)"/>
    </g>
  </svg>

  <ul class="contact-list">
    <li><svg viewBox="0 0 16 16"><path d="M4 0h8a1 1 0 0 1 1 1v14a1 1 0 0 1-1 1H4a1 1 0 0 1-1-1V1a1 1 0 0 1 1-1zm1 2v10h6V2z"/></svg>1-833-5GLEAMNG</li>
    <li><svg viewBox="0 0 16 16"><path d="M1 4c0-2 3-3 7-3s7 1 7 3v2h-4V4H5v2H1zM3 8h10l2 7H1z"/></svg>532-6264</li>
    <li><svg viewBox="0 0 16 16"><path d="M0 3h16v10H0zm2 2v1l6 4 6-4V5L8 9z"/></svg>info@gleamingpasses.example</li>
    <li><svg viewBox="0 0 16 16"><circle cx="8" cy="8" r="7.5"/></svg>www.gleamingpasses.example</li>
  </ul>
  <p class="address">418 Encore Avenue<br>Riverside, 902145.</p>

  <div class="brand">
    <span class="brand__mark" aria-hidden="true"></span>
    <span class="brand__name">Gleaming<br>Passes</span>
  </div>

  <div class="person">
    <p class="person__name">Wendel <span class="surname">Pike</span></p>
    <p class="person__role">Managing Director</p>
  </div>
</section>

<section class="card card--back" aria-label="Business card back">
  <svg class="card__shape" viewBox="0 0 673 416" aria-hidden="true">
    <path d="M27,0 H646 A27,27 0 0 0 673,27 V389 A27,27 0 0 0 646,416 H27 A27,27 0 0 0 0,389 V27 A27,27 0 0 0 27,0 Z" fill="var(--ink)"/>
  </svg>
  <p class="back-brand">Gleaming Passes</p>
</section>

</body>
</html>
```